Upmark Velo

We are a new start up company selling (online) innovative cycling products.
Being a new player in the market a modern eye catching logo would be good.
Initially selling safety tail lights with blinkers & modern designed cycling gloves and eventually extending our range into cycling clothing. Many of our products will have a safety theme.

Please see logo attached.
Updates

Project Deadline Extended
Reason: I have extended deadline because i have just received the Logo to be used.

Target Market(s)

We will be target marketing to the young 20-30year old trendy commuter cyclists to the 40 - 60 year old weekend road riders with there immaculate color coordinated road bikes & clothing.

Industry/Entity Type

Safety

Requirements
Must have
• Name: Liam Beck
Line for Mobile No. 0468 923 051
Line for email Address: liam@upmarkvelo.com.au
3 Lines for Postal Address: PO Box 3826
Harlow Vale Crossing
NSW 2157
Website: www.upmarkvelo.com.au

```html
<!DOCTYPE html>
<html lang="en">
<head>
<meta charset="utf-8">
<title>Upmark Velo – Business Cards</title>
<link href="https://fonts.googleapis.com/css2?family=Questrial&family=Montserrat:wght@600&display=swap" rel="stylesheet">
<style>
  :root {
    --stage: #e9e7e3;
    --card-light: #f7f7f5;
    --card-dark: #151515;
    --ink: #3b3b3b;
    --ink-soft: #5a5a5a;
    --accent: #f2a51f;
    --shadow: rgba(0, 0, 0, 0.18);
  }
  * { box-sizing: border-box; margin: 0; padding: 0; }
  html, body {
    width: 1200px;
    height: 1023px;
    overflow: hidden;
    background: var(--stage);
  }
  .canvas {
    position: relative;
    width: 1200px;
    height: 1023px;
  }
  .card {
    position: absolute;
    width: 560px;
    height: 320px;
    border-radius: 4px;
    box-shadow: 0 10px 28px var(--shadow);
  }
  /* Front card */
  .card--front {
    left: 60px;
    top: 100px;
    background: var(--card-light);
    padding: 44px 48px;
    font-family: "Questrial", sans-serif;
    color: var(--ink);
  }
  .brand {
    display: flex;
    align-items: center;
    gap: 12px;
    font-size: 34px;
    color: var(--ink);
    letter-spacing: 0.2px;
  }
  .brand__dot {
    width: 18px;
    height: 18px;
    border-radius: 50%;
    background: var(--accent);
  }
  .holder-name {
    margin-top: 22px;
    font-family: "Montserrat", sans-serif;
    font-weight: 600;
    font-size: 19px;
    letter-spacing: 1px;
    color: var(--accent);
    text-transform: uppercase;
  }
  .details {
    margin-top: 16px;
    display: grid;
    grid-template-columns: 1fr 1fr;
    gap: 0 20px;
    font-size: 14px;
    line-height: 1.55;
    color: var(--ink-soft);
  }
  .contact-list { list-style: none; }
  .contact-list li {
    display: flex;
    align-items: center;
    gap: 8px;
  }
  .contact-list svg {
    width: 13px;
    height: 13px;
    flex: none;
  }
  /* Back card */
  .card--back {
    left: 580px;
    top: 600px;
    background: var(--card-dark);
    display: flex;
    align-items: center;
    justify-content: center;
    font-family: "Questrial", sans-serif;
  }
  .card--back .brand {
    font-size: 46px;
    color: var(--accent);
  }
</style>
</head>
<body>
<main class="canvas">

  <section class="card card--front" aria-label="Business card front">
    <div class="brand">
      <span class="brand__dot"></span>
      <span class="brand__name">Upmark Velo</span>
    </div>
    <p class="holder-name">Liam Beck</p>
    <div class="details">
      <address class="postal" style="font-style: normal;">
        PO Box 3826<br>
        Harlow Vale Crossing<br>
        NSW 2157
      </address>
      <ul class="contact-list">
        <li>
          <svg viewBox="0 0 12 12" aria-hidden="true"><rect x="3" y="0.5" width="6" height="11" rx="1" fill="none" stroke="var(--accent)" stroke-width="1.2"/><circle cx="6" cy="9.6" r="0.7" fill="var(--accent)"/></svg>
          0468 923 051
        </li>
        <li>
          <svg viewBox="0 0 12 12" aria-hidden="true"><rect x="0.6" y="2.4" width="10.8" height="7.2" fill="var(--accent)"/><path d="M0.6 2.4 L6 6.6 L11.4 2.4" fill="none" stroke="#fff" stroke-width="1"/></svg>
          liam@upmarkvelo.com.au
        </li>
        <li>
          <svg viewBox="0 0 12 12" aria-hidden="true"><circle cx="6" cy="6" r="5.2" fill="none" stroke="var(--accent)" stroke-width="1.1"/><ellipse cx="6" cy="6" rx="2.2" ry="5.2" fill="none" stroke="var(--accent)" stroke-width="0.9"/><line x1="0.8" y1="6" x2="11.2" y2="6" stroke="var(--accent)" stroke-width="0.9"/></svg>
          www.upmarkvelo.com.au
        </li>
      </ul>
    </div>
  </section>

  <section class="card card--back" aria-label="Business card back">
    <div class="brand">
      <span class="brand__name">Upmark Velo</span>
    </div>
  </section>

</main>
</body>
</html>
```